Business Card for TLK Field Services

Would like a large logo on one side. On the other side, logo on one side and company phone number, address, and email on the other side. I don't have a logo so please create one for us.
Updates
I don't have a logo, so please create one for us.
Target Market(s)
Land Surveying
Industry/Entity Type
Surveyor
Contact Information for Business Card
Would like a large logo on one side. On the other side, logo on one side and company phone number, address, and email on the other side
Requirements
Nice to have
- would like the initials to be incorporated with the logo

```html
<!DOCTYPE html>
<html lang="en">
<head>
<meta charset="utf-8">
<title>TLK Field Services – Business Card</title>
<link href="https://fonts.googleapis.com/css2?family=Raleway:wght@400;500;600&display=swap" rel="stylesheet">
<style>
  :root {
    --ink: #0a0a0a;
    --gold: #ffd400;
    --gold-deep: #ffab00;
    --backdrop: #e9e6e1;
    --text-dark: #1a1a1a;
  }
  * { margin: 0; padding: 0; box-sizing: border-box; }
  html, body { width: 1200px; height: 913px; overflow: hidden; }
  body {
    background: var(--backdrop);
    font-family: "Raleway", sans-serif;
    position: relative;
  }
  .card {
    position: absolute;
    width: 540px;
    height: 309px;
    top: 302px;
    overflow: hidden;
    box-shadow: 0 8px 24px rgba(0,0,0,0.25);
  }
  .card--front { left: 40px; background: var(--ink); }
  .card--back { left: 620px; }

  .wordmark {
    position: absolute;
    color: var(--gold);
    font-weight: 600;
    text-transform: uppercase;
    white-space: nowrap;
  }
  .wordmark__name { display: block; line-height: 1; }
  .wordmark__tag { display: block; font-weight: 600; }

  .card--front .wordmark { left: 0; right: 0; top: 104px; text-align: center; }
  .card--front .wordmark__name { font-size: 92px; letter-spacing: 4px; }
  .card--front .wordmark__tag { font-size: 14px; letter-spacing: 12px; margin-top: 12px; padding-left: 12px; }

  .back-art { position: absolute; inset: 0; width: 100%; height: 100%; }

  .card--back .wordmark { right: 28px; top: 62px; text-align: right; }
  .card--back .wordmark__name { font-size: 46px; letter-spacing: 2px; }
  .card--back .wordmark__tag { font-size: 8px; letter-spacing: 5px; margin-top: 6px; }

  .contact {
    position: absolute;
    left: 34px;
    bottom: 34px;
    width: 250px;
    color: var(--text-dark);
    font-size: 15px;
    font-weight: 500;
    line-height: 1.25;
  }
  .contact__address { padding-bottom: 8px; border-bottom: 1px solid var(--text-dark); margin-bottom: 8px; }
  .contact__row { display: flex; align-items: center; gap: 7px; }
  .contact__row svg { width: 15px; height: 15px; flex: none; }
</style>
</head>
<body>

<section class="card card--front" aria-label="Business card front">
  <div class="wordmark">
    <span class="wordmark__name">TLK</span>
    <span class="wordmark__tag">Field Services</span>
  </div>
</section>

<section class="card card--back" aria-label="Business card back">
  <svg class="back-art" viewBox="0 0 540 309" preserveAspectRatio="none" aria-hidden="true">
    <defs>
      <linearGradient id="goldFade" x1="0" y1="0" x2="0" y2="1">
        <stop offset="0" stop-color="var(--gold)"/>
        <stop offset="1" stop-color="var(--gold-deep)"/>
      </linearGradient>
    </defs>
    <rect width="540" height="309" fill="url(#goldFade)"/>
    <path d="M232 0 Q300 190 540 222 L540 0 Z" fill="var(--ink)"/>
    <path d="M196 0 Q240 150 440 206 Q262 172 212 0 Z" fill="var(--ink)"/>
  </svg>

  <div class="wordmark">
    <span class="wordmark__name">TLK</span>
    <span class="wordmark__tag">Field Services</span>
  </div>

  <div class="contact">
    <p class="contact__address">41 Juniper Ave.<br>Boise, ID 83702</p>
    <p class="contact__row">
      <svg viewBox="0 0 16 16" aria-hidden="true"><circle cx="8" cy="8" r="7" fill="none" stroke="currentColor" stroke-width="1.2"/><path d="M5.5 4.5l1.3 1.6-.8 1c.5 1 1.2 1.7 2.2 2.2l1-.8 1.6 1.3-.8 1.2C8.1 11 5 7.9 4.3 5.3z" fill="currentColor"/></svg>
      0420 555 318
    </p>
    <p class="contact__row">
      <svg viewBox="0 0 16 16" aria-hidden="true"><rect x="1.5" y="3.5" width="13" height="9" fill="none" stroke="currentColor" stroke-width="1.2"/><path d="M1.5 3.5L8 9l6.5-5.5M1.5 12.5L6 8m8.5 4.5L10 8" fill="none" stroke="currentColor" stroke-width="1.2"/></svg>
      hello@tlkfield.com
    </p>
  </div>
</section>

</body>
</html>
```